Wirenexa

I'm looking to much improve our current website wirenexa.com
Updates

Low design quality

Target Market(s)

Commercial clients (Not-Residentials)

Industry/Entity Type

Office buildings and Industrial clients

Coding

Coded - Design and coding required

Number of Pages Required

5+ page

Requirements
Must have
• Very professional structured low voltage cabling projects for Wi-Fi, Audio/Video conference rooms, Access Control systems, CCTV.

```html
<!DOCTYPE html>
<html lang="en">
<head>
<meta charset="utf-8">
<title>Wirenexa – Contact</title>
<link href="https://fonts.googleapis.com/css2?family=Montserrat:wght@600;700&family=Roboto:wght@400;500;700&display=swap" rel="stylesheet">
<style>
:root{
  --red:#cc1f2b;
  --red-soft:#fbe9ea;
  --ink:#161b26;
  --text:#2b2f36;
  --muted:#626873;
  --line:#e3e5e9;
  --navy:#141a27;
  --navy-2:#1f2633;
  --band:#f5f6f8;
}
*{box-sizing:border-box;margin:0;padding:0}
html,body{width:1200px;height:2201px;overflow:hidden}
body{background:#f4f5f7;font-family:"Roboto",sans-serif;color:var(--text)}
.page{position:absolute;left:20px;top:20px;width:1160px;height:2164px;background:#fff;overflow:hidden}
.head{font-family:"Montserrat",sans-serif}

/* header */
.topbar{height:66px;display:flex;align-items:center;justify-content:space-between;padding:0 103px 0 84px;border-bottom:1px solid var(--line)}
.brand{display:flex;align-items:center;gap:6px;font-family:"Roboto",sans-serif;font-weight:700;font-size:24px;color:var(--ink);letter-spacing:-.3px}
.brand .mark{width:20px;height:20px;background:var(--red)}
.nav{display:flex;align-items:center;gap:26px;font-size:11px;color:#3a3f48}
.nav .on{color:var(--red)}
.btn-quote{background:var(--red);color:#fff;font-weight:500;font-size:11px;padding:9px 13px;border-radius:5px}

/* hero */
.hero{height:221px;background:linear-gradient(100deg,#262627 0%,#3a3a3b 40%,#4a3a33 62%,#7a4028 78%,#2a2a2b 100%);position:relative;padding:50px 0 0 102px;color:#fff}
.crumb{font-size:11px;color:#d0d0d0;display:flex;gap:8px}
.crumb b{color:#fff;font-weight:500}
.hero h1{font-family:"Montserrat",sans-serif;font-size:29px;font-weight:700;margin-top:14px}
.hero p{font-size:14px;line-height:23px;margin-top:12px;width:528px}

/* main */
.main{display:flex;gap:52px;padding:68px 102px 0 102px;height:1179px;border-top:6px solid #f4f5f7}
.left{width:536px}
.right{width:367px}
.card{background:#fff;border:1px solid #eceef1;border-radius:8px;box-shadow:0 4px 16px rgba(20,26,39,.07)}
.form-top{background:#fbfaf9;padding:26px 26px 28px;border-bottom:1px solid var(--line);border-radius:8px 8px 0 0}
.form-title{display:flex;align-items:center;gap:10px;font-family:"Montserrat",sans-serif;font-weight:600;font-size:19px;color:var(--ink)}
.ico-circle{width:32px;height:32px;border-radius:50%;background:var(--red-soft);display:flex;align-items:center;justify-content:center}
.form-top p{font-size:13px;color:var(--muted);margin-top:14px}
.form-body{padding:30px 26px 26px}
.row{display:flex;gap:20px;margin-bottom:22px}
.field{flex:1}
.field label{display:block;font-size:11px;font-weight:500;color:var(--ink);margin-bottom:10px}
.input{height:34px;border:1px solid #dcdfe4;border-radius:6px;padding:0 10px;font-size:11px;color:#6b717b;display:flex;align-items:center}
.textarea{height:119px;align-items:flex-start;padding-top:14px;padding-left:13px}
.privacy{border:1px dashed #d7dae0;background:#fafafa;border-radius:6px;padding:13px 14px;display:flex;gap:12px;font-size:9.5px;line-height:16px;color:#535964;margin-top:18px}
.send{margin-top:20px;height:39px;background:var(--red);border-radius:5px;color:#fff;font-weight:500;font-size:13px;display:flex;align-items:center;justify-content:center;gap:12px}

.faq{margin-top:64px}
.faq h2{font-family:"Montserrat",sans-serif;font-size:20px;font-weight:700;color:var(--ink);margin-bottom:26px}
.faq-item{border-bottom:1px solid var(--line);padding:14px 0}
.faq-item:first-of-type{padding-top:0}
.faq-q{display:flex;justify-content:space-between;align-items:center;font-family:"Montserrat",sans-serif;font-size:13px;color:var(--ink)}
.faq-a{font-size:11px;line-height:16px;color:var(--muted);margin-top:14px}

.support{background:var(--navy);border-radius:8px;padding:24px 26px;color:#fff;height:225px;position:relative;overflow:hidden;box-shadow:0 6px 16px rgba(20,26,39,.2)}
.support h3{font-family:"Montserrat",sans-serif;font-size:20px;font-weight:700}
.support .sub{font-size:11px;line-height:16px;color:#c3c7cf;margin-top:10px;width:300px;position:relative}
.srow{display:flex;align-items:center;gap:13px;margin-top:14px}
.sicon{width:39px;height:39px;border-radius:7px;background:#2a313e;display:flex;align-items:center;justify-content:center}
.slabel{font-size:9px;font-weight:700;color:#9aa0ab;letter-spacing:.4px}
.sval{font-size:15px;font-weight:700;margin-top:2px}
.support .big{position:absolute;right:28px;top:30px;opacity:.18}

.offices-h{margin-top:38px;border-left:3px solid var(--red);padding-left:15px;font-family:"Montserrat",sans-serif;font-size:17px;font-weight:700;color:var(--ink);height:22px;line-height:22px}
.office{margin-top:22px;height:350px;overflow:hidden;border-radius:8px}
.office + .office{margin-top:20px}
.photo{height:155px;position:relative}
.tag{position:absolute;right:14px;top:14px;background:var(--red);color:#fff;font-size:9.5px;font-weight:700;padding:4px 10px;border-radius:10px}
.office-body{padding:20px 20px}
.office-name{display:flex;align-items:center;gap:8px;font-weight:500;font-size:16px;color:var(--ink)}
.oline{display:flex;align-items:center;gap:10px;font-size:11px;color:#4b515b;margin-top:12px}
.oline:first-of-type{margin-top:16px}
.dir{margin-top:18px;height:32px;border:1px solid #dcdfe4;border-radius:6px;display:flex;align-items:center;justify-content:center;gap:14px;font-size:11px;font-weight:500;color:var(--ink)}

/* emergency */
.band{background:var(--band);height:273px;padding:66px 102px 0;border-top:1px solid var(--line)}
.emerg{background:#fff;border:1px solid #e6e8ec;border-radius:8px;height:152px;display:flex;align-items:center;padding:0 102px;gap:20px}
.emerg .ico{width:58px;height:58px;border-radius:8px;background:var(--red-soft);display:flex;align-items:center;justify-content:center;flex:none}
.emerg h3{font-family:"Montserrat",sans-serif;font-size:20px;font-weight:700;color:var(--ink)}
.emerg p{font-size:13px;line-height:21px;color:var(--muted);margin-top:8px;width:460px}
.hotline{margin-left:30px;background:var(--red);color:#fff;font-size:11px;font-weight:700;height:44px;width:166px;border-radius:5px;display:flex;align-items:center;justify-content:center;gap:10px;box-shadow:0 4px 10px rgba(204,31,43,.3);flex:none}

/* footer */
.footer{background:var(--navy);height:445px;padding:52px 84px 0;color:#c9cdd4}
.fcols{display:flex}
.fc1{width:258px}
.fc2{width:258px}
.fc3{width:254px}
.flogo{display:inline-flex;align-items:center;gap:5px;background:#e9e9e9;padding:6px 12px;font-weight:700;font-size:21px;color:var(--ink)}
.flogo .mark{width:17px;height:17px;background:var(--red)}
.fc1 p{font-size:11px;line-height:19px;margin-top:16px;width:225px}
.socials{display:flex;gap:12px;margin-top:28px}
.socials span{width:29px;height:29px;background:#f2f2f2;border-radius:4px}
.fh{font-family:"Montserrat",sans-serif;font-weight:700;font-size:15px;color:#fff;margin-top:6px}
.flist{list-style:none;margin-top:20px}
.flist li{font-size:11px;margin-bottom:12px;display:flex;gap:10px}
.flist li:before{content:"›";color:#8a909a}
.faddr{display:flex;gap:12px;margin-top:18px;font-size:11px;line-height:16px}
.faddr .k{font-size:8px;font-weight:700;color:#fff;letter-spacing:.4px;margin-bottom:4px}
.badge{width:103px;height:103px;background:#fff;border-radius:6px;display:flex;align-items:center;justify-content:center}
.badge span{width:64px;height:64px;border-radius:50%;background:#e6e8ec}
.cert{margin-top:26px;border:1px solid #2e3543;background:var(--navy-2);border-radius:8px;padding:20px 20px;font-size:11px;line-height:18.5px;width:219px}
.cert b{color:#fff}
.fbottom{margin-top:44px;border-top:1px solid #2c3340;padding-top:44px;display:flex;justify-content:space-between;font-size:9.5px;color:#9197a1}
.fbottom .links{display:flex;gap:20px;margin-left:140px}
</style>
</head>
<body>
<div class="page">

  <header class="topbar">
    <div class="brand"><span class="mark"></span>Wirenexa</div>
    <nav class="nav">
      <span>Home</span><span>About Us</span><span>Services</span><span class="on">Contact</span>
      <span class="btn-quote">Request a Quote</span>
    </nav>
  </header>

  <section class="hero" role="img" aria-label="Close-up photo of an orange network cable plugged into equipment">
    <div class="crumb"><span>Home</span><span>›</span><b>Contact Us</b></div>
    <h1>Get in Touch</h1>
    <p>Whether you need a full-scale network infrastructure or a simple residential repair, our expert team is ready to help you connect.</p>
  </section>

  <main class="main">
    <div class="left">
      <div class="card">
        <div class="form-top">
          <div class="form-title">
            <span class="ico-circle"><svg width="16" height="16" viewBox="0 0 24 24" fill="none" stroke="#cc1f2b" stroke-width="2"><path d="M4 5h16v11H9l-5 4z"/></svg></span>
            Request a Consultation
          </div>
          <p>Fill out the form below and one of our specialists will contact you within 24 hours.</p>
        </div>
        <div class="form-body">
          <div class="row">
            <div class="field"><label>Full Name</label><div class="input">John Doe</div></div>
            <div class="field"><label>Email Address</label><div class="input">john@example.com</div></div>
          </div>
          <div class="row">
            <div class="field"><label>Phone Number</label><div class="input">(555) 000-0000</div></div>
            <div class="field"><label>Company (Optional)</label><div class="input">Acme Corp</div></div>
          </div>
          <div class="row">
            <div class="field"><label>Service Interest</label><div class="input"></div></div>
          </div>
          <div class="field"><label>Project Details</label><div class="input textarea">Tell us about your requirements, timeline, and location...</div></div>
          <div class="privacy">
            <svg width="16" height="16" viewBox="0 0 24 24" fill="none" stroke="#2b2f36" stroke-width="2"><path d="M12 3l8 3v6c0 5-4 8-8 9-4-1-8-4-8-9V6z"/><path d="M8.5 12l2.5 2.5 4.5-5"/></svg>
            <span>Your data is safe with us. We use your information only to provide the requested consultation and never share it with third parties.</span>
          </div>
          <div class="send">Send Request
            <svg width="14" height="14" viewBox="0 0 24 24" fill="none" stroke="#fff" stroke-width="2"><path d="M22 2L11 13M22 2l-7 20-4-9-9-4z"/></svg>
          </div>
        </div>
      </div>

      <section class="faq">
        <h2>Frequently Asked Questions</h2>
        <div class="faq-item">
          <div class="faq-q">How quickly can I get an onsite estimate?<svg width="10" height="10" viewBox="0 0 24 24" fill="none" stroke="#161b26" stroke-width="3"><path d="M6 9l6 6 6-6"/></svg></div>
          <div class="faq-a">Typically, we can schedule an onsite consultation within 2-3 business days. For emergency repairs, we offer same-day response depending on location.</div>
        </div>
        <div class="faq-item"><div class="faq-q">Do you provide services outside of VA and MD?<svg width="10" height="10" viewBox="0 0 24 24" fill="none" stroke="#161b26" stroke-width="3"><path d="M6 9l6 6 6-6"/></svg></div></div>
        <div class="faq-item"><div class="faq-q">Is there a fee for a consultation?<svg width="10" height="10" viewBox="0 0 24 24" fill="none" stroke="#161b26" stroke-width="3"><path d="M6 9l6 6 6-6"/></svg></div></div>
      </section>
    </div>

    <aside class="right">
      <div class="support">
        <svg class="big" width="100" height="100" viewBox="0 0 24 24" fill="none" stroke="#8a93a6" stroke-width="1.6"><path d="M22 16.9v3a2 2 0 01-2.2 2 19.8 19.8 0 01-8.6-3.1 19.5 19.5 0 01-6-6A19.8 19.8 0 012.1 4.2 2 2 0 014.1 2h3a2 2 0 012 1.7c.1 1 .4 1.9.7 2.8a2 2 0 01-.5 2.1L8 9.8a16 16 0 006 6l1.3-1.3a2 2 0 012.1-.4c.9.3 1.8.6 2.8.7a2 2 0 011.7 2z"/></svg>
        <h3>Direct Support</h3>
        <p class="sub">Our expert technicians are available for direct calls during business hours.</p>
        <div class="srow" style="margin-top:20px">
          <span class="sicon"><svg width="18" height="18" viewBox="0 0 24 24" fill="none" stroke="#cc1f2b" stroke-width="2"><path d="M22 16.9v3a2 2 0 01-2.2 2 19.8 19.8 0 01-8.6-3.1 19.5 19.5 0 01-6-6A19.8 19.8 0 012.1 4.2 2 2 0 014.1 2h3a2 2 0 012 1.7c.1 1 .4 1.9.7 2.8a2 2 0 01-.5 2.1L8 9.8a16 16 0 006 6l1.3-1.3a2 2 0 012.1-.4c.9.3 1.8.6 2.8.7a2 2 0 011.7 2z"/></svg></span>
          <div><div class="slabel">CALL US TOLL-FREE</div><div class="sval head">(800) 555-0172</div></div>
        </div>
        <div class="srow">
          <span class="sicon"><svg width="18" height="18" viewBox="0 0 24 24" fill="none" stroke="#cc1f2b" stroke-width="2"><circle cx="12" cy="12" r="9"/><path d="M12 7v5l3 2"/></svg></span>
          <div><div class="slabel">BUSINESS HOURS</div><div class="sval">Mon - Fri: 8:00 AM - 6:00 PM</div></div>
        </div>
      </div>

      <h2 class="offices-h">Our Offices</h2>

      <div class="card office">
        <div class="photo" role="img" aria-label="Aerial photo of the Reston business district" style="background:linear-gradient(135deg,#3f5363,#6d7f8c 45%,#2f4450)"><span class="tag">Virginia</span></div>
        <div class="office-body">
          <div class="office-name"><svg width="16" height="16" viewBox="0 0 24 24" fill="none" stroke="#cc1f2b" stroke-width="2"><rect x="5" y="3" width="14" height="18"/><path d="M9 7h2M13 7h2M9 11h2M13 11h2M10 21v-4h4v4"/></svg>Reston Office</div>
          <div class="oline"><svg width="14" height="14" viewBox="0 0 24 24" fill="none" stroke="#cc1f2b" stroke-width="2"><path d="M12 22s7-6 7-12a7 7 0 00-14 0c0 6 7 12 7 12z"/><circle cx="12" cy="10" r="2.5"/></svg>5200 Ridgeway Plaza, Suite 300, Reston, VA 20191</div>
          <div class="oline"><svg width="14" height="14" viewBox="0 0 24 24" fill="none" stroke="#cc1f2b" stroke-width="2"><path d="M22 16.9v3a2 2 0 01-2.2 2 19.8 19.8 0 01-8.6-3.1 19.5 19.5 0 01-6-6A19.8 19.8 0 012.1 4.2 2 2 0 014.1 2h3a2 2 0 012 1.7c.1 1 .4 1.9.7 2.8a2 2 0 01-.5 2.1L8 9.8a16 16 0 006 6l1.3-1.3a2 2 0 012.1-.4c.9.3 1.8.6 2.8.7a2 2 0 011.7 2z"/></svg>(703) 555-0167</div>
          <div class="oline"><svg width="14" height="14" viewBox="0 0 24 24" fill="none" stroke="#cc1f2b" stroke-width="2"><rect x="3" y="5" width="18" height="14" rx="2"/><path d="M3 7l9 6 9-6"/></svg>va-office@wirenexa.com</div>
          <div class="dir">Get Directions <span>›</span></div>
        </div>
      </div>

      <div class="card office">
        <div class="photo" role="img" aria-label="Photo of the Baltimore harbor skyline" style="background:linear-gradient(180deg,#b9d3dc,#6f8e97 55%,#44575c)"><span class="tag">Maryland</span></div>
        <div class="office-body">
          <div class="office-name"><svg width="16" height="16" viewBox="0 0 24 24" fill="none" stroke="#cc1f2b" stroke-width="2"><rect x="5" y="3" width="14" height="18"/><path d="M9 7h2M13 7h2M9 11h2M13 11h2M10 21v-4h4v4"/></svg>Baltimore Office</div>
          <div class="oline"><svg width="14" height="14" viewBox="0 0 24 24" fill="none" stroke="#cc1f2b" stroke-width="2"><path d="M12 22s7-6 7-12a7 7 0 00-14 0c0 6 7 12 7 12z"/><circle cx="12" cy="10" r="2.5"/></svg>310 Pierline Avenue, Baltimore, MD 21231</div>
          <div class="oline"><svg width="14" height="14" viewBox="0 0 24 24" fill="none" stroke="#cc1f2b" stroke-width="2"><path d="M22 16.9v3a2 2 0 01-2.2 2 19.8 19.8 0 01-8.6-3.1 19.5 19.5 0 01-6-6A19.8 19.8 0 012.1 4.2 2 2 0 014.1 2h3a2 2 0 012 1.7c.1 1 .4 1.9.7 2.8a2 2 0 01-.5 2.1L8 9.8a16 16 0 006 6l1.3-1.3a2 2 0 012.1-.4c.9.3 1.8.6 2.8.7a2 2 0 011.7 2z"/></svg>(410) 555-0139</div>
          <div class="oline"><svg width="14" height="14" viewBox="0 0 24 24" fill="none" stroke="#cc1f2b" stroke-width="2"><rect x="3" y="5" width="18" height="14" rx="2"/><path d="M3 7l9 6 9-6"/></svg>md-office@wirenexa.com</div>
          <div class="dir">Get Directions <span>›</span></div>
        </div>
      </div>
    </aside>
  </main>

  <section class="band">
    <div class="emerg">
      <span class="ico"><svg width="30" height="30" viewBox="0 0 24 24" fill="none" stroke="#cc1f2b" stroke-width="2"><circle cx="12" cy="12" r="9"/><path d="M12 7v6M12 16.5v.5"/></svg></span>
      <div>
        <h3>Need Emergency Network Support?</h3>
        <p>We provide 24/7 critical infrastructure support for enterprise clients. If your business is facing a complete network outage, call our priority line immediately.</p>
      </div>
      <span class="hotline"><svg width="8" height="8" viewBox="0 0 24 24" fill="#fff"><circle cx="12" cy="12" r="6"/></svg>Emergency Hotline</span>
    </div>
  </section>

  <footer class="footer">
    <div class="fcols">
      <div class="fc1">
        <div class="flogo"><span class="mark"></span>Wirenexa</div>
        <p>The Mid-Atlantic's premier provider of specialized low-voltage infrastructure since 1994. Quality, reliability, and precision in every connection.</p>
        <div class="socials"><span></span><span></span><span></span><span></span></div>
      </div>
      <div class="fc2">
        <div class="fh">Services</div>
        <ul class="flist">
          <li>Commercial Cabling</li><li>Fiber Optic Installation</li><li>Security &amp; CCTV</li><li>VOIP &amp; Audio Visual</li><li>Wi-Fi Site Surveys</li>
        </ul>
      </div>
      <div class="fc3">
        <div class="fh">Our Offices</div>
        <div class="faddr"><svg width="14" height="14" viewBox="0 0 24 24" fill="none" stroke="#cc1f2b" stroke-width="2"><path d="M12 22s7-6 7-12a7 7 0 00-14 0c0 6 7 12 7 12z"/><circle cx="12" cy="10" r="2.5"/></svg><div><div class="k">MAIN OFFICE (VA)</div>4410 Linden Park Dr, Suite 210,<br>Vienna, VA 22180</div></div>
        <div class="faddr" style="margin-top:22px"><svg width="14" height="14" viewBox="0 0 24 24" fill="none" stroke="#cc1f2b" stroke-width="2"><path d="M12 22s7-6 7-12a7 7 0 00-14 0c0 6 7 12 7 12z"/><circle cx="12" cy="10" r="2.5"/></svg><div><div class="k">REGIONAL OFFICE (MD)</div>7720 Harwick Lane,<br>Columbia, MD 21045</div></div>
        <div class="faddr" style="margin-top:22px"><svg width="14" height="14" viewBox="0 0 24 24" fill="none" stroke="#cc1f2b" stroke-width="2"><path d="M22 16.9v3a2 2 0 01-2.2 2 19.8 19.8 0 01-8.6-3.1 19.5 19.5 0 01-6-6A19.8 19.8 0 012.1 4.2 2 2 0 014.1 2h3a2 2 0 012 1.7c.1 1 .4 1.9.7 2.8a2 2 0 01-.5 2.1L8 9.8a16 16 0 006 6l1.3-1.3a2 2 0 012.1-.4c.9.3 1.8.6 2.8.7a2 2 0 011.7 2z"/></svg><div>Local: (703) 555-0180<br>National: (888) 555-0144</div></div>
        <div class="faddr" style="margin-top:20px"><svg width="14" height="14" viewBox="0 0 24 24" fill="none" stroke="#cc1f2b" stroke-width="2"><rect x="3" y="5" width="18" height="14" rx="2"/><path d="M3 7l9 6 9-6"/></svg><div>sales@wirenexa.com</div></div>
      </div>
      <div class="fc4">
        <div class="badge" role="img" aria-label="Anniversary badge"><span></span></div>
        <div class="cert">Wirenexa is a proud employer of <b>Certified Network Distribution Designers (CNDD)</b>, ensuring industry-leading standards on every installation.</div>
      </div>
    </div>
    <div class="fbottom">
      <span>© 2024 Wirenexa. All Rights Reserved. Licensed in VA, MD &amp; DC.</span>
      <span class="links"><span>Privacy Policy</span><span>Terms of Service</span><span>Sitemap</span></span>
      <span>Powered by Northline Systems</span>
    </div>
  </footer>

</div>
</body>
</html>
```